依頼詳細
不動産の案内所や現地、宣伝用に置けるような「のぼり旗」を作成したいと思います。
観光スポットなどをドライブしながらでも違和感のない感じだとありがたいです。
目には止まって欲しいけどリゾート地に設置したいのでカチカチなデザインでない方が良いです。
記載項目
碧浜ソレイユ、ロゴ、0995−61−2348、
※海が見える売土地あります

※この部分は変えられるようにしたいです。
・海が見える売物件
・管理地
・不動産案内所
・売地募集中
・不動産のことならお気軽にどうぞ
希望イメージ
シンプル 複雑
単色 カラフル
暗い 明るい
日常 高級
遊び心 厳粛
未来的 伝統的
女性的 男性的
希望する色
青系、水色系
納品ファイル
• イラストレーター形式 (.ai)
補足説明
その他、掲載した方が良い文字や表現などありましたら追加していただいて大丈夫です。
サイズを掲載するのを忘れましたが標準の横600×縦1800mmで考えております。
中身の文字は臨機応変に変更しようかと思っております。
よろしくお願いいたします。
■ 選んだ理由

リゾート地に設置した際にイメージに合いながらも目を引きそうな感じがとても気に入りました。

■ 提案者全員のお礼・コメント

とても素敵なデザインありがとうございました!!
貴重なお時間をかけて考えていただき感謝いたします。
また機会がありましたらぜひよろしくお願いいたします。

```html
<!DOCTYPE html>
<html lang="ja">
<head>
<meta charset="utf-8">
<title>碧浜ソレイユ のぼり旗</title>
<link rel="stylesheet" href="https://fonts.googleapis.com/css2?family=Noto+Sans+JP:wght@500;700;900&family=Barlow+Semi+Condensed:wght@600&display=swap">
<style>
  :root {
    --navy: #1b6cc2;
    --sky: #2aa9e8;
    --sky-soft: #cfeaf8;
    --panel: #ffffff;
    --ink: #1a5fae;
  }
  html, body { margin: 0; padding: 0; overflow: hidden; background: #fff; }
  .flag {
    position: relative;
    width: 1200px; height: 3396px;
    overflow: hidden;
    background: linear-gradient(90deg, var(--navy) 0 50%, var(--sky) 50% 100%);
    font-family: "Noto Sans JP", sans-serif;
  }
  .panel {
    position: absolute;
    left: 140px; top: 80px; width: 920px; height: 2980px;
    background: var(--panel);
  }
  .panel-tint {
    position: absolute; left: 0; top: 0; width: 100%; height: 1500px;
    background: linear-gradient(180deg, var(--sky-soft) 0%, var(--panel) 100%);
  }
  .sea-band {
    position: absolute; left: 0; top: 2900px; width: 1200px; height: 160px;
    background: linear-gradient(180deg, var(--sky-soft) 0%, #8fd0f1 100%);
  }
  .brand-mark {
    position: absolute; left: 600px; top: 210px; transform: translateX(-50%);
    display: flex; flex-direction: column; align-items: center; gap: 20px;
  }
  .brand-mark .dot {
    width: 240px; height: 240px; border-radius: 50%;
    background: var(--sky);
  }
  .brand-mark .name {
    font-size: 40px; font-weight: 700; color: var(--ink); letter-spacing: 4px;
  }
  .vertical { position: absolute; writing-mode: vertical-rl; white-space: nowrap; }
  .company {
    left: 500px; top: 700px;
    font-size: 200px; font-weight: 900; color: var(--ink);
    line-height: 1; letter-spacing: 6px;
  }
  .tagline {
    left: 275px; top: 700px;
    font-size: 74px; font-weight: 500; color: var(--ink);
    line-height: 1; letter-spacing: 62px;
  }
  .offer {
    position: absolute; left: 804px; top: 690px; width: 240px; height: 1540px;
    border-radius: 120px; background: var(--sky);
    display: flex; justify-content: center; align-items: center;
  }
  .offer span {
    writing-mode: vertical-rl; white-space: nowrap;
    font-size: 100px; font-weight: 700; color: #fff; line-height: 1; letter-spacing: 16px;
  }
  .contact {
    position: absolute; left: 0; top: 3060px; width: 1200px; height: 336px;
    background: var(--navy);
    color: #fff; text-align: center;
    font-family: "Barlow Semi Condensed", sans-serif; font-weight: 600;
  }
  .contact .tel { font-size: 124px; line-height: 1; margin-top: 70px; letter-spacing: 3px; }
  .contact .web { font-size: 82px; line-height: 1; margin-top: 18px; letter-spacing: 1px; }
</style>
</head>
<body>
<div class="flag">
  <div class="panel">
    <div class="panel-tint" role="img" aria-label="淡い水色の背景の模様"></div>
  </div>

  <div class="sea-band" role="img" aria-label="海の波を表す帯"></div>

  <div class="brand-mark">
    <div class="dot"></div>
    <div class="name">碧浜ソレイユ</div>
  </div>

  <div class="vertical tagline">海の見える土地専門の不動産屋さん</div>
  <div class="vertical company">碧浜ソレイユ株式会社</div>
  <div class="offer"><span>海が見える売土地あります</span></div>

  <div class="contact">
    <div class="tel">TEL 0995-61-2348</div>
    <div class="web">www.aohama-soleil.com</div>
  </div>
</div>
</body>
</html>
```